Detail Shop Business card design

i need a business card design for my new detailing company called 'Brenner's Detail Shop'. i want an all black and white design . simple, direct and to the point. i want the designer to choose a fitting font to match the logothe front should have logo, address, phone and email and the back side should have a slogan and text indicating that we offer services on anything including cars, trucks, motorcycles and RVs. slogan will read "we take pride in your ride"
maybe also very small on the back side the IG icon with Brenners_Detail_Shop

phone 482.615.7734
address 7384 E Harlow Ave
Spokane WA 99342
email: BrennersDetail@quorvail.com

Target Market(s)

all ages , auto enthusiasts

Industry/Entity Type

Automotive

Contact Information for Business Card

the front should have logo, address, phone and email and the back side should have a slogan and text indicating that we offer services on anything including cars, trucks, motorcycles and RVs. slogan will read "we take pride in your ride"

phone 482.615.7734
address 7384 E Harlow Ave
Spokane WA 99342

Colors
000000
ffffff

Requirements
Must have
• bold font and very simple design with good spacing
Nice to have
• anything creative from the designer indicating we service any types of vehicles
Should not have
• any colors ,

```html
<!DOCTYPE html>
<html lang="en">
<head>
<meta charset="utf-8">
<title>Brenner's Detail Shop – Business Card</title>
<link rel="stylesheet" href="https://fonts.googleapis.com/css2?family=Arimo:wght@700&family=Open+Sans:ital,wght@1,300&display=swap">
<style>
  :root {
    --ink: #000000;
    --paper: #ffffff;
    --card-grey: #3a3a3a;
    --band-mid: #d9d9d9;
  }
  html, body {
    margin: 0;
    padding: 0;
    width: 1200px;
    height: 720px;
    overflow: hidden;
    background: var(--card-grey);
  }
  .card {
    position: relative;
    width: 1200px;
    height: 720px;
    background: var(--card-grey);
    overflow: hidden;
  }
  .frame-bands {
    position: absolute;
    inset: 0;
    width: 1200px;
    height: 720px;
  }
  .brand-mark {
    position: absolute;
    left: 34px;
    top: 78px;
    width: 180px;
    display: flex;
    flex-direction: column;
    align-items: center;
    gap: 12px;
  }
  .brand-mark__dot {
    width: 78px;
    height: 78px;
    border-radius: 50%;
    background: var(--paper);
  }
  .brand-mark__name {
    font-family: "Arimo", Arial, sans-serif;
    font-weight: 700;
    font-size: 21px;
    line-height: 1.15;
    color: var(--paper);
    text-align: center;
  }
  .title-band {
    position: absolute;
    left: 0;
    top: 403px;
    width: 1200px;
    height: 79px;
    background: linear-gradient(90deg, var(--paper) 0%, var(--band-mid) 45%, rgba(255,255,255,0.25) 72%, rgba(255,255,255,0) 88%);
  }
  .shop-name {
    position: absolute;
    left: 32px;
    top: 403px;
    margin: 0;
    height: 79px;
    line-height: 79px;
    font-family: "Arimo", Arial, sans-serif;
    font-weight: 700;
    font-size: 60px;
    letter-spacing: -2.5px;
    color: var(--ink);
    text-transform: uppercase;
    white-space: nowrap;
  }
  .contact {
    position: absolute;
    left: 32px;
    top: 502px;
    margin: 0;
    font-family: "Open Sans", "Segoe UI", sans-serif;
    font-style: italic;
    font-weight: 300;
    font-size: 40px;
    line-height: 48px;
    color: var(--paper);
  }
  .contact span { display: block; white-space: nowrap; }
</style>
</head>
<body>
  <main class="card">
    <svg class="frame-bands" viewBox="0 0 1200 720" aria-hidden="true">
      <polygon points="0,0 1200,0 1200,62 440,62 408,27 0,27" fill="var(--ink)"/>
      <polygon points="0,656 763,656 795,693 1200,693 1200,720 0,720" fill="var(--ink)"/>
    </svg>

    <div class="brand-mark">
      <div class="brand-mark__dot"></div>
      <div class="brand-mark__name">Brenner's<br>Detail Shop</div>
    </div>

    <div class="title-band"></div>
    <h1 class="shop-name">Brenner's Detail Shop</h1>

    <address class="contact">
      <span>7384 E Harlow Ave</span>
      <span>Spokane WA 99342</span>
      <span>BrennersDetail@quorvail.com</span>
    </address>
  </main>
</body>
</html>
```